Interior designer needs a gorgeous, chic business card design.

A new, small Interior Design firm needs a business card that is chic, contemporary and elegant. Nothing over the top. My interiors are contemporary classic with an elegant feel to them. I like to use quality finishes and products rather than follow the latest fads. Projects can be anything from Pre start selections, bathrooms, kitchens, bedrooms, custom upholstery, furniture, rugs and art etc. The final design should display quality and an achievable sense of chic. I am open to all colours including black but not limited to this.

```html
<!DOCTYPE html>
<html lang="en">
<head>
<meta charset="utf-8">
<title>Interior Design Specialist – Business Card</title>
<link rel="stylesheet" href="https://fonts.googleapis.com/css2?family=Cutive+Mono&display=swap">
<style>
  :root {
    --page: #ffffff;
    --card-centre: #ffffff;
    --card-edge: #d6d6d6;
    --back-centre: #f7f8f8;
    --back-edge: #dfe4e5;
    --ink: #1e1e1e;
    --ink-soft: #333333;
    --accent-teal: #7cc7cc;
    --ornament-teal: #9cc9c6;
    --ornament-grey: #b9bcbc;
  }
  * { margin: 0; padding: 0; box-sizing: border-box; }
  html, body {
    width: 1200px;
    height: 900px;
    overflow: hidden;
    background: var(--page);
  }
  .canvas {
    position: relative;
    width: 1200px;
    height: 900px;
  }
  .card {
    position: absolute;
    left: 227px;
    width: 708px;
    height: 404px;
    overflow: hidden;
    font-family: "Cutive Mono", "Courier New", monospace;
    color: var(--ink);
  }
  .card--front {
    top: 25px;
    background: radial-gradient(ellipse at 50% 45%, var(--card-centre) 0%, #f3f3f3 50%, var(--card-edge) 100%);
  }
  .card--back {
    top: 465px;
    background: radial-gradient(ellipse at 50% 50%, var(--back-centre) 0%, #eef1f1 55%, var(--back-edge) 100%);
  }
  .cartouche {
    position: absolute;
    inset: 0;
    width: 708px;
    height: 404px;
  }
  .identity {
    position: absolute;
    left: 220px;
    top: 170px;
    width: 268px;
    text-align: center;
  }
  .identity__name {
    font-size: 36px;
    font-weight: 400;
    line-height: 1;
    letter-spacing: 0.5px;
    white-space: nowrap;
  }
  .identity__rule {
    display: block;
    margin: 8px 0 6px;
    border-top: 2px dotted var(--accent-teal);
  }
  .identity__role {
    font-size: 16px;
    letter-spacing: 1.2px;
    color: var(--ink-soft);
    white-space: nowrap;
  }
  .damask-field {
    position: absolute;
    inset: 0;
    background: linear-gradient(180deg, rgba(210,225,228,0.35) 0%, rgba(255,255,255,0) 45%, rgba(255,255,255,0) 60%, rgba(210,225,228,0.35) 100%);
  }
  .contact {
    position: absolute;
    left: 0;
    right: 0;
    top: 155px;
    text-align: center;
    list-style: none;
    font-size: 33px;
    line-height: 31px;
    letter-spacing: 0.5px;
  }
</style>
</head>
<body>
<main class="canvas">
  <section class="card card--front" aria-label="Business card front">
    <svg class="cartouche" viewBox="0 0 708 404" role="img" aria-label="Floral vine cartouche ornament with teal leaves framing the name">
      <defs>
        <linearGradient id="vineTone" x1="0" y1="0" x2="1" y2="1">
          <stop offset="0" stop-color="var(--ornament-teal)"/>
          <stop offset="0.5" stop-color="var(--ornament-grey)"/>
          <stop offset="1" stop-color="var(--ornament-teal)"/>
        </linearGradient>
      </defs>
      <path d="M354,90 C340,55 320,40 305,38 C290,80 240,110 140,115 C100,140 90,200 110,250 C120,300 150,340 210,360 C260,330 310,300 354,300 C398,300 448,330 498,360 C558,340 588,300 598,250 C618,200 608,140 568,115 C468,110 418,80 403,38 C388,40 368,60 354,90 Z"
            fill="none" stroke="url(#vineTone)" stroke-width="26" stroke-linejoin="round" opacity="0.55"/>
    </svg>
    <div class="identity">
      <h1 class="identity__name">Your Name Here</h1>
      <span class="identity__rule"></span>
      <p class="identity__role">Interior Design Specialist</p>
    </div>
  </section>

  <section class="card card--back" aria-label="Business card back">
    <div class="damask-field" role="img" aria-label="Faint pale blue damask wallpaper pattern"></div>
    <ul class="contact">
      <li>This is the address</li>
      <li>This is the website</li>
      <li>This is the phone number</li>
    </ul>
  </section>
</main>
</body>
</html>
```